Wadi Alsafeer
Wadi Alsafeer - Construction
Creative Brief
Simple
Salem Dabbagh
CEO
Locality 428 - Alley 17 - House 9 Al Dhaheera - Baghdad - Iraq
ceo@wadialsafeer.com
www.wadialsafeer.com
rokba72x rokba72x
i uploaded the final files so you all can work now with it and very soon I'll chose a winner
and i wont you to make these changes in the latter head only: 1- add the address in Arabic language ( محلة 428 - زقاق 17 - دار 9) and 2- change the e-mail into ( info@wadialsafeer.com ) thank you
Hello , great job all i just wont you to add the name and title in English and Arabic language in the businesses cards only, ( name in Arabic : سالم دباغ) and the title(CEO) in Arabic ( المدير المفوض) Regards,

```html
<!DOCTYPE html>
<html lang="en">
<head>
<meta charset="utf-8">
<title>Wadi Alsafeer – Stationery</title>
<link rel="stylesheet" href="https://fonts.googleapis.com/css2?family=Open+Sans:wght@400;600;700&family=Playfair+Display:wght@500&family=Noto+Naskh+Arabic:wght@400;600&display=swap">
<style>
  :root {
    --backdrop: #e6e7e9;
    --brand-blue: #1f6fd8;
    --brand-blue-deep: #1658b6;
    --slate: #3b3e44;
    --paper: #ffffff;
    --ink: #2a2c30;
    --muted: #6b6f76;
    --notebook: #1b1c1f;
  }
  * { box-sizing: border-box; margin: 0; padding: 0; }
  html, body { width: 1200px; height: 787px; overflow: hidden; }
  body {
    background: var(--backdrop);
    font-family: "Open Sans", Arial, sans-serif;
    color: var(--ink);
    position: relative;
  }
  .arabic { font-family: "Noto Naskh Arabic", "Open Sans", serif; direction: rtl; unicode-bidi: isolate; }
  .piece { position: absolute; background: var(--paper); box-shadow: 0 2px 6px rgba(0,0,0,.12); overflow: hidden; }

  /* wordmark */
  .wordmark { display: inline-flex; align-items: center; gap: 5px; font-weight: 700; color: var(--brand-blue); white-space: nowrap; }
  .wordmark__square { width: 9px; height: 9px; background: var(--slate); }
  .wordmark--light { color: #fff; }
  .wordmark--light .wordmark__square { background: #fff; }
  .wordmark--dim { color: #6c6f75; }
  .wordmark--dim .wordmark__square { background: #6c6f75; }

  /* contact band */
  .contact-band {
    position: absolute; left: 0; right: 0; bottom: 0;
    background: var(--brand-blue); color: #fff;
    display: flex; align-items: center; gap: 10px;
    padding: 0 50px 0 10px; font-size: 5.6px; white-space: nowrap;
  }
  .contact-band::after {
    content: ""; position: absolute; right: 0; top: 0; bottom: 0; width: 44px;
    background: var(--slate); clip-path: polygon(40% 0, 100% 0, 100% 100%, 0 100%);
  }
  .contact-band::before {
    content: ""; position: absolute; left: 0; right: 0; top: -3px; height: 1px; background: var(--brand-blue);
  }
  .contact-item { display: inline-flex; align-items: center; gap: 3px; }
  .contact-item svg { width: 6px; height: 6px; fill: #fff; flex: none; }

  /* business card front */
  .card-front { left: 60px; top: 340px; width: 330px; height: 190px; }
  .card-front .wordmark { position: absolute; left: 0; right: 0; top: 40px; justify-content: center; font-size: 15px; }
  .card-front__name { position: absolute; left: 0; right: 0; top: 88px; text-align: center; font-family: "Playfair Display", Georgia, serif; font-size: 12px; font-weight: 500; letter-spacing: 2px; color: var(--brand-blue-deep); }
  .card-front__name-ar { position: absolute; left: 0; right: 0; top: 104px; text-align: center; font-size: 10px; font-weight: 600; color: var(--brand-blue-deep); }
  .card-front__title { position: absolute; left: 0; right: 0; top: 127px; text-align: center; font-size: 6.5px; letter-spacing: 1px; color: var(--muted); display: flex; justify-content: center; gap: 6px; }
  .card-front__title .arabic { font-size: 7px; letter-spacing: 0; }
  .card-front .contact-band { height: 20px; gap: 14px; padding-right: 52px; }

  /* business card back */
  .card-back { left: 60px; top: 110px; width: 330px; height: 190px; background: var(--brand-blue); }
  .card-back svg.card-back__corner { position: absolute; inset: 0; }
  .card-back .wordmark { position: absolute; left: 0; right: 0; top: 84px; justify-content: center; font-size: 17px; }

  /* letterhead */
  .letterhead { left: 440px; top: 46px; width: 320px; height: 452px; }
  .letterhead .wordmark { position: absolute; left: 0; right: 0; top: 28px; justify-content: center; font-size: 14px; }
  .letter-body { position: absolute; left: 34px; right: 34px; top: 80px; font-size: 5.6px; line-height: 1.65; color: #45484e; }
  .letter-body p { margin-bottom: 7px; text-align: justify; }
  .letter-sign { position: absolute; left: 0; right: 0; top: 322px; text-align: center; font-size: 5.6px; line-height: 1.6; color: #45484e; }
  .letter-sign strong { font-weight: 600; color: var(--ink); }
  .letterhead .contact-band {
    height: 26px; bottom: 12px;
    display: grid; grid-template-columns: auto auto; column-gap: 14px; row-gap: 1px;
    align-content: center; justify-content: start; padding-right: 50px;
  }
  .letterhead .contact-item .arabic { font-size: 6px; }

  /* envelope */
  .envelope { left: 420px; top: 540px; width: 360px; height: 190px; }
  .envelope svg.envelope__flap { position: absolute; left: 0; top: 0; }
  .envelope .contact-band { height: 12px; bottom: 12px; right: 90px; font-size: 4.6px; }
  .envelope .wordmark { position: absolute; right: 10px; bottom: 12px; font-size: 10px; }

  /* notebook */
  .notebook { left: 830px; top: 150px; width: 290px; height: 400px; background: var(--notebook); border-radius: 6px; }
  .notebook .wordmark { position: absolute; left: 0; right: 0; top: 186px; justify-content: center; font-size: 15px; }
</style>
</head>
<body>

  <section class="piece card-back" aria-label="Business card back">
    <svg class="card-back__corner" width="330" height="190" viewBox="0 0 330 190">
      <polygon points="0,120 0,190 90,190" fill="#ffffff"/>
      <polygon points="0,100 0,120 90,190 112,190" fill="var(--slate)"/>
    </svg>
    <span class="wordmark wordmark--light"><span class="wordmark__square"></span>Wadi Alsafeer</span>
  </section>

  <section class="piece card-front" aria-label="Business card front">
    <span class="wordmark"><span class="wordmark__square"></span>Wadi Alsafeer</span>
    <h1 class="card-front__name">SALEM DABBAGH</h1>
    <p class="card-front__name-ar arabic" lang="ar">سالم دباغ</p>
    <p class="card-front__title"><span>CEO</span><span>|</span><span class="arabic" lang="ar">المدير المفوض</span></p>
    <div class="contact-band">
      <span class="contact-item"><svg viewBox="0 0 10 10"><path d="M2 0h2l1 3-1.5 1a6 6 0 0 0 2.5 2.5L7 5l3 1v2c0 1-1 2-2 2C4 10 0 6 0 2c0-1 1-2 2-2z"/></svg>+964 780 555 0142</span>
      <span class="contact-item"><svg viewBox="0 0 10 10"><path d="M0 2h10v6H0zM0 2l5 3.5L10 2"/></svg>ceo@wadialsafeer.com</span>
      <span class="contact-item"><svg viewBox="0 0 10 10"><circle cx="5" cy="5" r="4.5"/></svg>www.wadialsafeer.com</span>
    </div>
  </section>

  <section class="piece letterhead" aria-label="Letterhead">
    <span class="wordmark"><span class="wordmark__square"></span>Wadi Alsafeer</span>
    <div class="letter-body">
      <p>Dear Sir or Madam,</p>
      <p>Thank you for your interest in our construction services. We are pleased to share an overview of our current projects and the team that delivers them across Baghdad and the region.</p>
      <p>Our engineers plan every site with care, from early surveys to final handover, and we keep clients informed at each stage so that budgets and timelines stay clear.</p>
      <p>We look forward to working with you and welcome any questions about the proposal enclosed with this letter.</p>
    </div>
    <div class="letter-sign">
      <strong>Salem Dabbagh</strong><br>CEO<br>www.wadialsafeer.com
    </div>
    <div class="contact-band">
      <span class="contact-item"><svg viewBox="0 0 10 10"><path d="M5 0a3.5 3.5 0 0 0-3.5 3.5C1.5 6 5 10 5 10s3.5-4 3.5-6.5A3.5 3.5 0 0 0 5 0zm0 5a1.5 1.5 0 1 1 0-3 1.5 1.5 0 0 1 0 3z"/></svg>Locality 428 - Alley 17 - House 9 Al Dhaheera</span>
      <span class="contact-item"><svg viewBox="0 0 10 10"><path d="M2 0h2l1 3-1.5 1a6 6 0 0 0 2.5 2.5L7 5l3 1v2c0 1-1 2-2 2C4 10 0 6 0 2c0-1 1-2 2-2z"/></svg>+964 780 555 0142</span>
      <span class="contact-item"><svg viewBox="0 0 10 10"><path d="M5 0a3.5 3.5 0 0 0-3.5 3.5C1.5 6 5 10 5 10s3.5-4 3.5-6.5A3.5 3.5 0 0 0 5 0zm0 5a1.5 1.5 0 1 1 0-3 1.5 1.5 0 0 1 0 3z"/></svg><span class="arabic" lang="ar">محلة 428 - زقاق 17 - دار 9</span></span>
      <span class="contact-item"><svg viewBox="0 0 10 10"><path d="M0 2h10v6H0zM0 2l5 3.5L10 2"/></svg>info@wadialsafeer.com</span>
    </div>
  </section>

  <section class="piece envelope" aria-label="Envelope">
    <svg class="envelope__flap" width="360" height="190" viewBox="0 0 360 190">
      <polygon points="0,0 360,0 180,105" fill="var(--brand-blue)"/>
      <polygon points="0,0 180,105 150,0" fill="var(--brand-blue-deep)" opacity=".35"/>
    </svg>
    <div class="contact-band">
      <span class="contact-item">+964 780 555 0142</span>
      <span class="contact-item">Al Dhaheera - Baghdad</span>
      <span class="contact-item">www.wadialsafeer.com</span>
    </div>
    <span class="wordmark"><span class="wordmark__square"></span>Wadi Alsafeer</span>
  </section>

  <section class="piece notebook" aria-label="Notebook cover">
    <span class="wordmark wordmark--dim"><span class="wordmark__square"></span>Wadi Alsafeer</span>
  </section>

</body>
</html>
```